Maple Syrup Bottle (front) Label design

I need label design for a 16fl OZ rectangular bottle of maple syrup with the usable dimensions of: Front: 4" x 2" and the back area for "ingredient specifications" of: 6" x 2". The maple syrup product comes from our own farm and is a quality product. The technical name/class of the syrup is: Grade A / AMBER
Updates

I can’t seem to find a way to upload a photo of the maple syrup bottle, but the front dimensions are clearly written on bottle description. Again: 4.5” by 2.25”

I have tried to upload the photo of the maple syrup bottle several times, and it seems (from my side) that it is successful. But I can never find it and the artists cannot find it either. Not sure what to do.

I have tried several times to add a photo of maple bottle, but it never shows up

This seems to be a futile exercise

I would like to post some images of the actual quill Hollow (not the one on Fendix, though!
But I can’t get back to the page that allows that to happen. Please advise!

Somebody PLEASE ask PW management to make it possible for me to upload more images! The "add photos" etc. just disappears from anywhere.

Target Market(s)

High-end food stores

Industry/Entity Type

Maple syrup retail industry

Other font styles liked:
• I don't know, and welcome suggestions

Colors

Designer to choose colors to be used in the design.

Requirements
Must have
• Name of Farm: Quill Hollow Maple
Nice to have
• The label can be "minimalist" and elegant. There is already a Maple leaf glass relief on the top of front of the bottle.
Should not have
• and NOT include farm buildings with steam coming out the chimney, etc.

```html
<!DOCTYPE html>
<html lang="en">
<head>
<meta charset="utf-8">
<title>Quill Hollow Maple – Front Label</title>
<link rel="stylesheet" href="https://fonts.googleapis.com/css2?family=Montserrat:wght@500&family=Old+Standard+TT:wght@700&display=swap">
<style>
  :root {
    --label-ground: #050505;
    --label-ink: #f4f4f4;
    --rule-ink: #d9d9d9;
  }
  html, body {
    margin: 0;
    padding: 0;
    width: 1200px;
    height: 751px;
    overflow: hidden;
    background: var(--label-ground);
  }
  .label {
    position: relative;
    width: 1200px;
    height: 751px;
    background: var(--label-ground);
  }
  .label-art {
    position: absolute;
    inset: 0;
    width: 1200px;
    height: 751px;
  }
  .farm-name,
  .volume {
    font-family: "Old Standard TT", Georgia, serif;
    font-weight: 700;
    fill: var(--label-ink);
  }
  .farm-name { font-size: 30px; }
  .volume { font-size: 23px; }
  .product-name {
    position: absolute;
    left: 700px;
    width: 400px;
    top: 352px;
    margin: 0;
    text-align: center;
    white-space: nowrap;
    font-family: "Montserrat", Arial, sans-serif;
    font-weight: 500;
    font-size: 41px;
    letter-spacing: -0.3px;
    color: var(--label-ink);
    line-height: 1;
  }
  .grade {
    position: absolute;
    left: 787px;
    width: 228px;
    top: 435px;
    height: 55px;
    margin: 0;
    box-sizing: border-box;
    border-top: 1px solid var(--rule-ink);
    border-bottom: 1px solid var(--rule-ink);
    text-align: center;
    white-space: nowrap;
    line-height: 53px;
    font-family: "Old Standard TT", Georgia, serif;
    font-weight: 700;
    font-size: 24px;
    color: var(--label-ink);
  }
</style>
</head>
<body>
  <main class="label">
    <svg class="label-art" viewBox="0 0 1200 751" xmlns="http://www.w3.org/2000/svg">
      <defs>
        <path id="crown-arc" d="M 762 305 A 138 138 0 0 1 1038 305"/>
        <path id="base-arc" d="M 785 530 A 118 118 0 0 0 1015 530"/>
      </defs>
      <text class="farm-name" text-anchor="middle">
        <textPath href="#crown-arc" startOffset="50%" textLength="410" lengthAdjust="spacing">QUILL HOLLOW MAPLE</textPath>
      </text>
      <circle class="farm-mark" cx="900" cy="278" r="24" fill="var(--label-ink)"/>
      <text class="volume" text-anchor="middle">
        <textPath href="#base-arc" startOffset="50%" textLength="245" lengthAdjust="spacing">16 fluid Oz /463 mL</textPath>
      </text>
    </svg>
    <h1 class="product-name">MAPLE SYRUP</h1>
    <p class="grade">Grade A / AMBER</p>
  </main>
</body>
</html>
```